Pause Your Day And Browse- PYDB poster

I am the Vice President of Advocacy for the Coastline Shelfkeepers Guild. I am looking to have a set of posters made for PYDB (Pause Your Day and Browse) October 23. PYDB is a time when all school children in BC are encouraged to Pause Your Day and Browse for 15-20 minutes at some point in their day.

I would like to get a set of 2 digital posters designed (if possible it would be nice to have the option to print to both 11 x 17 and 8.5 x 11 paper). We need a poster that is high school (Grade 8-12) appropriate and one that is elementary (Grade k-7) appropriate. Both posters need to be replicated in French. All posters need to have the KWNU logo on them as well as the Coastline Shelfkeepers Guild Logo.

Here is a link to last year's successful design http://kwnu-example.org/csg/info/advocacy.html
There are two additional samples in the uploaded files section.

Each poster needs to have the following information:

-Pause Your Day and Browse (PYDB)
- The date Monday, October 23, 2017
-the logo for the KWNU (attached)
-the logo for the CSG (attached)- the logos do not have to be large.

Target Market(s)

Children ages 5-12 and 12-17 as well as their teachers

Industry/Entity Type

Teacher

Font styles to use
Sans Serif

Requirements
Must have
• Must have both logos- colours may be changed for either or both
Nice to have
• Clear, Bright lettering. Images of child or children enjoying reading
Should not have
• stereotypes

```html
<!DOCTYPE html>
<html lang="en">
<head>
<meta charset="utf-8">
<title>Pause Your Day and Browse – Poster</title>
<link rel="stylesheet" href="https://fonts.googleapis.com/css2?family=Anton&family=Open+Sans:wght@400&display=swap">
<style>
  :root {
    --paper: #ffffff;
    --green: #006837;
    --navy: #253f8a;
    --sage: #8cc68a;
    --page-light: #e8d8bd;
    --page-mid: #b58a55;
    --page-dark: #6b4a2a;
    --figure: #9a9a9a;
  }
  html, body {
    margin: 0;
    padding: 0;
    overflow: hidden;
    background: var(--paper);
  }
  .poster {
    position: relative;
    width: 776px;
    height: 1200px;
    background: var(--paper);
    overflow: hidden;
  }
  .mark {
    position: absolute;
    display: flex;
    align-items: center;
    gap: 10px;
    font-family: "Anton", sans-serif;
    color: var(--green);
    font-size: 34px;
    line-height: 1;
  }
  .mark--guild { left: 62px; top: 60px; }
  .mark--guild .mark__shape {
    width: 46px; height: 46px; background: var(--sage);
  }
  .mark--union { right: 22px; top: 30px; color: var(--navy); }
  .mark--union .mark__shape {
    width: 112px; height: 112px; border-radius: 50%; background: var(--navy);
    order: 2;
  }
  .headline {
    position: absolute;
    left: 0; top: 0;
    width: 776px; height: 1200px;
  }
  .headline text { font-family: "Anton", sans-serif; }
  .acronym { fill: url(#pages); }
  .title { fill: var(--green); }
  .date {
    position: absolute;
    left: 96px;
    top: 770px;
    width: 650px;
    margin: 0;
    font-family: "Open Sans", sans-serif;
    font-weight: 400;
    font-size: 51px;
    letter-spacing: -1px;
    color: var(--green);
    white-space: nowrap;
  }
</style>
</head>
<body>
  <main class="poster">
    <div class="mark mark--guild"><span class="mark__shape"></span>CSG</div>
    <div class="mark mark--union">KWNU<span class="mark__shape"></span></div>

    <svg class="headline" viewBox="0 0 776 1200" aria-labelledby="headline-title">
      <title id="headline-title">PYDB – Pause Your Day and Browse</title>
      <defs>
        <linearGradient id="pages" x1="0" y1="0" x2="1" y2="1">
          <stop offset="0" stop-color="var(--page-light)"/>
          <stop offset="0.35" stop-color="var(--page-mid)"/>
          <stop offset="0.65" stop-color="var(--page-dark)"/>
          <stop offset="1" stop-color="var(--page-mid)"/>
        </linearGradient>
      </defs>
      <text class="acronym" x="66" y="490" font-size="245" textLength="688" lengthAdjust="spacingAndGlyphs">PYDB</text>
      <g role="img" aria-label="Illustration of a child sitting cross-legged, reading an open book">
        <rect x="318" y="322" width="170" height="205" rx="40" fill="var(--figure)"/>
      </g>
      <text class="title" x="90" y="600" font-size="104" textLength="664" lengthAdjust="spacingAndGlyphs">Pause Your Day</text>
      <text class="title" x="66" y="762" font-size="184" textLength="688" lengthAdjust="spacingAndGlyphs">and Browse</text>
    </svg>

    <p class="date">Monday, October 23, 2017</p>
  </main>
</body>
</html>
```